" Atendemos de maneira integrada em reabilitação ,tanto odontológica como neurológica. Somos terapia ocupacional, fonoaudiologia, neuropediatria e odontologia. Trabalhamos com técnicas de ponta e muito proximidade com nossos pacientes e suas famílias. "

```html
<!DOCTYPE html>
<html lang="pt-BR">
<head>
<meta charset="UTF-8">
<title>Vitalente – Cartão de visita</title>
<link rel="stylesheet" href="https://fonts.googleapis.com/css2?family=Fira+Sans:wght@400;500;700&display=swap">
<style>
  :root {
    --page-bg: #ecebe8;
    --navy-dark: #0f2d4f;
    --navy-mid: #1d4a76;
    --navy-text: #2f4f7a;
    --sky: #7fc2e6;
    --leaf: #7cbf5a;
    --white: #ffffff;
    --faint: #e9ecef;
    --body-text: #33476b;
  }
  * { box-sizing: border-box; margin: 0; padding: 0; }
  html, body {
    width: 1200px; height: 1200px; overflow: hidden;
    background: var(--page-bg);
    font-family: "Fira Sans", sans-serif;
  }
  .sheet {
    width: 1200px; height: 1200px;
    display: flex; flex-direction: column; align-items: center; justify-content: center;
    gap: 80px;
  }
  .card {
    width: 800px; height: 460px;
    border-radius: 48px;
    position: relative; overflow: hidden;
    box-shadow: 0 6px 18px rgba(0,0,0,0.12);
  }
  /* Front */
  .card-front {
    background: radial-gradient(ellipse at 60% 35%, var(--navy-mid) 0%, var(--navy-dark) 75%);
    display: flex; flex-direction: column; align-items: center; justify-content: center;
    padding-left: 60px;
  }
  .brand-mark {
    width: 96px; height: 96px; border-radius: 50%;
    background: var(--leaf);
    margin-bottom: 26px;
  }
  .brand-name {
    color: var(--white); font-weight: 700; font-size: 62px; letter-spacing: 1px; line-height: 1;
  }
  .brand-partners {
    color: var(--sky); font-weight: 400; font-size: 25px; margin-top: 8px;
  }
  /* Back */
  .card-back { background: var(--white); }
  .back-decoration {
    position: absolute; left: -60px; top: 60px;
    width: 430px; height: 430px; border-radius: 50%;
    background: var(--faint);
  }
  .accent-bar {
    position: absolute; right: 22px; top: 120px;
    width: 8px; height: 190px; background: var(--leaf); opacity: 0.8;
  }
  .holder {
    position: absolute; right: 90px; top: 70px; text-align: right; color: var(--navy-text);
  }
  .holder-name { font-size: 27px; font-weight: 400; }
  .holder-role { font-size: 27px; font-weight: 400; }
  .contact-list {
    position: absolute; right: 50px; top: 200px;
    list-style: none; text-align: right; color: var(--body-text);
    font-size: 21px; line-height: 30px;
  }
  .contact-list li { display: flex; justify-content: flex-end; align-items: center; gap: 14px; }
  .contact-list .icon { width: 16px; height: 16px; flex: none; }
  .contact-list .no-icon { width: 16px; flex: none; }
</style>
</head>
<body>
<main class="sheet">
  <section class="card card-front" aria-label="Frente do cartão">
    <div class="brand-mark" aria-hidden="true"></div>
    <h1 class="brand-name">VITALENTE</h1>
    <p class="brand-partners">Paulo Andrade &amp; Helena Rocha</p>
  </section>

  <section class="card card-back" aria-label="Verso do cartão">
    <div class="back-decoration" role="img" aria-label="Marca da clínica em tom claro como fundo decorativo"></div>
    <div class="accent-bar" aria-hidden="true"></div>
    <div class="holder">
      <p class="holder-name">Nome Sobrenome</p>
      <p class="holder-role">função</p>
    </div>
    <ul class="contact-list">
      <li>vitalente
        <svg class="icon" viewBox="0 0 16 16" aria-hidden="true"><circle cx="8" cy="8" r="7" fill="var(--body-text)"/></svg>
      </li>
      <li>contato@contato.com
        <svg class="icon" viewBox="0 0 16 16" aria-hidden="true"><rect x="1" y="3" width="14" height="10" rx="1" fill="var(--body-text)"/><path d="M1.5 4 L8 9 L14.5 4" stroke="#fff" stroke-width="1.4" fill="none"/></svg>
      </li>
      <li>(00)0000-0000
        <svg class="icon" viewBox="0 0 16 16" aria-hidden="true"><path d="M3 1.5 L6 1.5 L7 5 L5.2 6.3 C6 8.3 7.7 10 9.7 10.8 L11 9 L14.5 10 L14.5 13 C14.5 14 13.5 14.6 12.5 14.5 C6.5 14 2 9.5 1.5 3.5 C1.4 2.5 2 1.5 3 1.5 Z" fill="var(--body-text)"/></svg>
      </li>
      <li>rua sem nome,00 Bairro Sem Nome
        <svg class="icon" viewBox="0 0 16 16" aria-hidden="true"><path d="M8 15 C8 15 2.5 9 2.5 6 A5.5 5.5 0 0 1 13.5 6 C13.5 9 8 15 8 15 Z" fill="var(--body-text)"/><circle cx="8" cy="6" r="2" fill="#fff"/></svg>
      </li>
      <li>Cidade Sem Nome <span class="no-icon"></span></li>
    </ul>
  </section>
</main>
</body>
</html>
```